Website Revamp for 7Q Distributor

Morvix Pte Ltd (http://morvix.com.sg/about.php) is a 7Q authorized distributor located in Singapore.

The revamp hopes to move the look & feel of the website from a corporate/industrial feel to one that is more homely/interior-design, so as to attract architects, home-builders, interior-designers with a more up-market design.
Updates

If product images are required, please use images from www.morvix.com.sg. Thanks!

For newsletter signup, just a link at the header will do, as we will be implementing additional profiling fields in the signup form.

Target Market(s)

Hopes to attract architects, home-builders, interior-designers with a more up-market design.

Industry/Entity Type

Industrial

Requirements
Must have
• Refer to brief document

```html
<!DOCTYPE html>
<html lang="en">
<head>
<meta charset="utf-8">
<title>Morvix Pte Ltd — 7Q Authorized Distributor</title>
<link href="https://fonts.googleapis.com/css2?family=Roboto+Condensed:wght@400;700;800&family=Roboto:wght@300;400;700&display=swap" rel="stylesheet">
<style>
:root{
  --dark:#262626;
  --blue:#0089d9;
  --blue-deep:#0a6db5;
  --brand-blue:#1a8fde;
  --red:#d90010;
  --red-deep:#a8000c;
  --white:#ffffff;
  --ink:#111111;
  --tab-light:#e9e9e9;
}
*{margin:0;padding:0;box-sizing:border-box}
html,body{width:1200px;height:1040px;overflow:hidden}
body{position:relative;background:var(--blue);font-family:"Roboto",Arial,sans-serif;color:var(--white)}
a{color:inherit;text-decoration:none}
.abs{position:absolute}

.masthead{position:absolute;left:0;top:0;width:1200px;height:478px;background:var(--dark);border-bottom:2px solid var(--red)}
.brand{left:125px;top:8px;font-family:"Roboto Condensed",sans-serif;font-weight:800;font-size:44px;letter-spacing:1px;color:var(--brand-blue);line-height:1}

.main-nav{left:0;top:0}
.main-nav a{position:absolute;top:21px;font-family:"Roboto Condensed",sans-serif;font-weight:700;font-size:19px;line-height:24px;white-space:nowrap}
.main-nav .is-section{color:var(--brand-blue)}
.main-nav .is-open{top:16px;left:703px;width:125px;height:32px;padding-top:5px;text-align:center;background:linear-gradient(#e8101d,#b8000b);border:1px solid #ff4a4a;border-radius:14px}
.nav-caret{left:732px;top:48px;width:0;height:0;border-left:7px solid transparent;border-right:7px solid transparent;border-bottom:12px solid #e00010;z-index:6}

.dropdown{z-index:5;font-family:"Roboto Condensed",sans-serif;font-weight:700;font-size:14px}
.dropdown.primary{left:702px;top:60px;width:202px;height:160px;background:linear-gradient(#dc0010,#a5000b);border-radius:14px;border:1px solid #ff3b3b}
.dropdown.secondary{left:903px;top:69px;width:153px;height:69px;background:linear-gradient(#dc0010,#b0000b);border-radius:0 14px 14px 0;border:1px solid #ff3b3b}
.dropdown a{position:absolute;left:14px;white-space:nowrap}
.dropdown .is-active{left:0;width:200px;height:21px;padding-left:14px;padding-top:3px;background:var(--red-deep)}
.dropdown.secondary .top{left:0;width:151px;height:24px;padding-left:12px;padding-top:6px;background:var(--red-deep);top:0}

.slider{left:126px;top:104px;width:959px;height:352px;background:var(--white)}
.slide-photo{left:10px;top:12px;width:938px;height:328px;background:linear-gradient(125deg,#0b2c55 0%,#2a6bb0 40%,#8fc0ea 58%,#dceaf6 70%,#4b86c4 85%,#143a6a 100%)}
.slide-caption{left:10px;top:280px;width:938px;height:60px;background:rgba(40,40,40,.72);font-size:14px;padding:22px 16px}
.slide-caption b{font-weight:700}
.dots{left:812px;top:300px}
.dots span{position:absolute;top:0;width:19px;height:19px;border-radius:50%;background:#2a2a2a}
.dots .on{background:#1d3d6b;border:2px solid #21a0f0}

.tabs{top:456px;height:42px;font-family:"Roboto Condensed",sans-serif;font-weight:700;font-size:19px;text-align:center;padding-top:9px;box-shadow:0 3px 5px rgba(0,0,0,.35)}
.tab-products{left:411px;width:183px;background:linear-gradient(#1a1a1a,#000);color:var(--white)}
.tab-portfolio{left:598px;width:183px;background:linear-gradient(#ffffff,var(--tab-light));color:#222}

.section-title{font-weight:300;font-size:30px;line-height:1}
.section-title em{font-style:normal;color:var(--red)}
.hot-title{left:139px;top:548px}

.card{top:604px;width:204px}
.card .thumb{width:204px;height:141px;border:4px solid #f4f4f4;box-shadow:0 1px 3px rgba(0,0,0,.3)}
.card h3{margin-top:18px;padding-left:3px;font-weight:400;font-size:15px}
.card p{margin-top:11px;padding-left:3px;font-size:11px;line-height:20px}
.card .more{display:block;margin-top:5px;padding-left:3px;font-size:12px;font-weight:700}
.thumb-room{background:linear-gradient(135deg,#f2e6c1,#cfae7a 60%,#8a5c32)}
.thumb-tower{background:linear-gradient(135deg,#6b9a4e,#c9d6de 45%,#e6e3e0 70%,#9a7c73)}
.thumb-lounge{background:linear-gradient(135deg,#6a4a35,#c9a888 45%,#efe5d8 70%,#5b3a26)}

.divider-v{left:820px;top:545px;width:2px;height:345px;background:linear-gradient(transparent,rgba(0,60,120,.35),transparent)}

.subscribe-title{left:844px;top:548px}
.subscribe-sub{left:844px;top:581px;font-size:14px}
.email{left:845px;top:614px;width:228px;height:33px;background:var(--blue-deep);border-top:2px solid #075895;font-style:italic;font-size:14px;padding:8px 11px;color:#d8ecfa}
.submit{left:897px;top:666px;width:116px;height:33px;border-radius:17px;background:linear-gradient(#ffffff,#cfcfcf);box-shadow:0 2px 3px rgba(0,0,0,.3);color:#222;text-align:center;font-family:"Roboto Condensed",sans-serif;font-weight:700;font-size:18px;padding-top:5px}

.partner{left:851px;top:718px;color:var(--ink);font-family:"Roboto Condensed",sans-serif}
.partner .mark{font-weight:700;font-size:28px;line-height:30px}
.partner .desc{font-weight:400;font-size:15px;line-height:16px;margin-top:7px}
.member-badge{left:853px;top:812px;width:197px;height:46px;background:#0b2540;border-radius:4px}

.footer-rule{left:136px;top:964px;width:940px;height:2px;background:rgba(0,70,140,.35)}
.copyright{left:137px;top:987px;font-size:11px}
.footer-nav{top:987px;right:126px;font-size:11px;white-space:nowrap}
.footer-nav a{margin-left:16px}
</style>
</head>
<body>

<header class="masthead">
  <div class="abs brand">MORVIX</div>
</header>

<nav class="abs main-nav">
  <a href="#" style="left:476px">Home</a>
  <a href="#" class="is-section" style="left:563px">The Philosophy</a>
  <a href="#" class="is-open">Our Solutions</a>
  <a href="#" style="left:860px">Our Portfolios</a>
  <a href="#" style="left:1006px">Contact Us</a>
</nav>

<section class="abs slider">
  <div class="abs slide-photo" role="img" aria-label="Upward view of a glass office tower against a blue sky"></div>
  <div class="abs slide-caption"><b>Morbi dapibus</b> mauris nec nunc facilisis vitae posuere massa faucibus.</div>
  <div class="abs dots">
    <span style="left:0"></span><span style="left:28px"></span><span class="on" style="left:56px;width:22px;height:22px;top:-1px"></span><span style="left:82px"></span>
  </div>
</section>

<div class="abs nav-caret"></div>
<div class="abs dropdown primary">
  <a href="#" class="is-active" style="top:13px">Glass &amp; Glazing</a>
  <a href="#" style="top:44px">Building Services</a>
  <a href="#" style="top:72px">Filtration</a>
  <a href="#" style="top:100px">Automotives</a>
  <a href="#" style="top:128px">Others</a>
</div>
<div class="abs dropdown secondary">
  <a href="#" class="top">Sun Control Films</a>
  <a href="#" style="left:12px;top:35px">Safety Films</a>
</div>

<a href="#" class="abs tabs tab-products">Featured Products</a>
<a href="#" class="abs tabs tab-portfolio">Featured Portfolio</a>

<h2 class="abs section-title hot-title">What’s <em>hot?</em></h2>

<article class="abs card" style="left:136px">
  <div class="thumb thumb-room" role="img" aria-label="Sunlit living room with white sofa and wooden floor"></div>
  <h3>Lorem Ipsum</h3>
  <p>Etiam eros sem, viverra non placerat eget, ullamcorper nec leo. Proin quis tortor a ante convallis</p>
  <a href="#" class="more">Read More</a>
</article>
<article class="abs card" style="left:361px">
  <div class="thumb thumb-tower" role="img" aria-label="Modern glass building with palm trees"></div>
  <h3>Lorem Ipsum</h3>
  <p>Etiam eros sem, viverra non placerat eget, ullamcorper nec leo. Proin quis tortor a ante convallis</p>
  <a href="#" class="more">Read More</a>
</article>
<article class="abs card" style="left:589px">
  <div class="thumb thumb-lounge" role="img" aria-label="Spacious lounge with large windows and sofas"></div>
  <h3>Lorem Ipsum</h3>
  <p>Etiam eros sem, viverra non placerat eget, ullamcorper nec leo. Proin quis tortor a ante convallis</p>
  <a href="#" class="more">Read More</a>
</article>

<div class="abs divider-v"></div>

<h2 class="abs section-title subscribe-title">Subscribe</h2>
<div class="abs subscribe-sub">for a newsletter</div>
<div class="abs email">Email Address</div>
<a href="#" class="abs submit">SUBMIT</a>

<div class="abs partner">
  <div class="mark">7Q</div>
  <div class="desc">Authorized Distributor<br>Architectural and Interior Solutions</div>
</div>
<div class="abs member-badge" role="img" aria-label="Industry association membership badge"></div>

<div class="abs footer-rule"></div>
<div class="abs copyright">© Copyright 2010 Morvix Pte Ltd. All Rights Reserved.</div>
<nav class="abs footer-nav">
  <a href="#">The Philosophy</a><a href="#">Our Solutions</a><a href="#">Our Portfolios</a><a href="#">Contact Us</a><a href="#">Site Map</a>
</nav>

</body>
</html>
```